Webdesign for an Health & Beauty Center

We need a new modern and elegant web design for the relaunch of the http://veskarin.at/ website.
The website is for a company which offer all services for a beuty center like epilation, cosmetics and more.
The new website should use big emotional background images and a modern menu.
All in all the website should give a female expression and the design should be clear and not playful.
The existing logo used be used for the new design, the base colours of the existing website could be used optionally.

Reason: Review of the designs together with the customer needs a little more time.

Industry/Entity Type
It Company
Look and feel
Each slider illustrates characteristics of the customer's brand and the style your logo design should communicate.

```html
<!DOCTYPE html>
<html lang="en">
<head>
<meta charset="utf-8">
<title>Veskarin – Health &amp; Beauty Center</title>
<link href="https://fonts.googleapis.com/css2?family=Open+Sans:wght@300;400;600&family=Tinos:wght@700&family=Arimo:wght@400&display=swap" rel="stylesheet">
<style>
:root{
  --nav-bg:#dfcfb2;
  --nav-text:#5a2e14;
  --white:#ffffff;
  --accent-red:#c0242b;
  --dark-text:#3c3c3c;
  --gold:#8a6d3b;
  --logo-gold:#b59a63;
  --heading-grey:#5a5a5a;
  --body-text:#555049;
  --content-bg-top:#f3efea;
  --content-bg-bottom:#ebe3da;
  --footer-bg:#636363;
  --footer-text:#ffffff;
  --rule:#bdb2a3;
}
*{margin:0;padding:0;box-sizing:border-box}
html,body{width:1033px;height:1200px;overflow:hidden}
body{position:relative;background:var(--white);font-family:'Arimo',Arial,sans-serif;color:var(--body-text)}
.abs{position:absolute}

.main-nav{left:0;top:0;width:1033px;height:51px;background:var(--nav-bg)}
.main-nav a{position:absolute;top:19px;font:600 11.2px/14px 'Open Sans',sans-serif;letter-spacing:.5px;color:var(--nav-text);text-decoration:none}

.site-header{left:0;top:51px;width:1033px;height:93px;background:var(--white)}
.call-us{left:85px;top:35px;font:300 22px/28px 'Open Sans',sans-serif;color:var(--dark-text)}
.call-us span{color:var(--accent-red)}
.brand{left:452px;top:28px;display:flex;align-items:center;gap:8px}
.brand-mark{width:22px;height:22px;border-radius:50%;background:var(--logo-gold)}
.brand-name{font:300 32px/36px 'Open Sans',sans-serif;letter-spacing:3px;color:var(--logo-gold)}
.social{left:859px;top:41px;display:flex;gap:9px}
.social span{width:22px;height:22px;border-radius:50%;background:radial-gradient(circle at 40% 35%,#e24a4a,#b11d22);box-shadow:0 2px 2px rgba(0,0,0,.25)}

.hero{left:0;top:144px;width:1033px;height:348px;background:linear-gradient(90deg,#f6f6f6 0%,#f2efed 30%,#e9c9b4 50%,#eccfbd 65%,#f1e6df 80%,#f4f4f4 100%)}
.hero-caption{left:84px;top:216px;width:286px;height:95px;background:rgba(243,243,243,.9);text-align:center}
.hero-caption .kicker{position:absolute;left:0;right:0;top:15px;font:400 20.5px/24px 'Open Sans',sans-serif;color:var(--dark-text)}
.hero-caption .title{position:absolute;left:0;right:0;top:40px;font:300 36px/42px 'Open Sans',sans-serif;color:var(--gold)}

.content{left:0;top:497px;width:1033px;height:603px;background:linear-gradient(180deg,var(--content-bg-top),var(--content-bg-bottom))}
.section-title{font:700 22px/26px 'Tinos',Georgia,serif;color:var(--heading-grey);letter-spacing:.3px}
.about-photo{left:86px;top:100px;width:252px;height:156px;border:3px solid var(--white);border-radius:5px;background:linear-gradient(135deg,#d9cfc6,#f2e6dc 40%,#e3b89c 65%,#c9a98f);box-shadow:0 6px 6px -4px rgba(0,0,0,.25)}
.about-copy{left:368px;top:100px;width:334px}
.about-copy h2{font:400 15.5px/21.5px 'Open Sans',sans-serif;color:var(--gold);margin-bottom:4px}
.about-copy p{font-size:11.2px;line-height:19px}
.about-copy h3{font:400 10.8px/17px 'Arimo',Arial,sans-serif;color:var(--gold);margin:6px 0 4px}
.divider{left:744px;top:101px;height:360px;border-left:1px dotted var(--rule)}
.category-list{left:775px;top:96px;width:172px;list-style:none}
.category-list li{height:24.1px;line-height:24px;border-bottom:1px dotted var(--rule);font-size:10.8px;color:var(--body-text);padding-left:18px;position:relative}
.category-list li:last-child{border-bottom:none}
.category-list li::before{content:"»";position:absolute;left:5px;top:-1px;color:#777}

.site-footer{left:0;top:1099px;width:1033px;height:101px;background:var(--footer-bg);border-top:2px solid var(--white);color:var(--footer-text);font-size:10.8px}
.footer-left{left:86px;top:30px;line-height:19px}
.footer-right{right:133px;top:13px;line-height:18.7px;text-align:right}
</style>
</head>
<body>

<nav class="main-nav abs">
  <a style="left:85px">HOME</a>
  <a style="left:156px">CATEGORIES</a>
  <a style="left:274px">FAQ'S</a>
  <a style="left:350px">GALLERY</a>
  <a style="left:440px">SHOPPING CART</a>
  <a style="left:574px">OUR PARTNERS</a>
  <a style="left:703px">CONTACT US</a>
  <a style="left:817px">SITEMAP</a>
</nav>

<header class="site-header abs">
  <div class="call-us abs"><span>Call Us :</span> +123 555 0142</div>
  <div class="brand abs"><span class="brand-mark"></span><span class="brand-name">veskarin</span></div>
  <div class="social abs"><span></span><span></span><span></span></div>
</header>

<section class="hero abs" role="img" aria-label="Hero photo of a relaxed woman with a white towel and a calla lily">
  <div class="hero-caption abs">
    <div class="kicker">SPECIAL CARE</div>
    <div class="title">SOLUTIONS</div>
  </div>
</section>

<main class="content abs">
  <h1 class="section-title abs" style="left:86px;top:59px">ABOUT US!</h1>
  <div class="about-photo abs" role="img" aria-label="Photo of a facial mask treatment at the beauty center"></div>
  <article class="about-copy abs">
    <h2>PELLENTESQUE HABITANT MORBI TRISTIQUE SENECTUS ET NETUS ET MALESUADA FAMES</h2>
    <p>Pellentesque habitant morbi tristique senectus et netus et malesuada fames ac turpis egestas. Vestibulum tortor quam, feugiat vitae, ultricies eget, tempor sit amet, ante. Donec eu libero sit amet quam egestas semper. Aenean ultricies mi vitae est. Mauris placerat eleifend leo. Quisque sit amet est et sapien ullamcorper pharetra. Vestibulum erat wisi, condimentum sed, commodo vitae,</p>
    <h3>EXERCITATION ULLAMCO LABORIS NISI UT ALIQUIP EX EA COMMODO CONSEQUAT. OREM IPSUM DOLOR SIT AMET</h3>
    <p>Lorem ipsum dolor sit amet, consectetur adipisicing elit, sed do eiusmod tempor incididunt ut labore et dolore magna aliqua. Ut enim ad minim veniam, quis nostrud exercitation ullamco laboris nisi ut aliquip ex ea commodo consequat. Duis aute irure dolor in reprehenderit in voluptate velit esse cillum dolore eu fugiat nulla pariatur.Lorem ipsum dolor sit amet, consectetur adipisicing elit, sed do eiusmod tempor incididunt</p>
  </article>
  <div class="divider abs"></div>
  <h1 class="section-title abs" style="left:773px;top:59px">CATEGORIES!</h1>
  <ul class="category-list abs">
    <li>Bdarlnatur ferode</li>
    <li>Ndtasader certasa</li>
    <li>Derlpasya xertytsas</li>
    <li>Ndtasader certasa</li>
    <li>Derlpasya xertytsas</li>
    <li>Bdarlnatur ferode</li>
    <li>Consec Teer Adsiping</li>
    <li>Phasellus hendrerit</li>
    <li>Donec ultricies</li>
    <li>Vivamus sollicitudin</li>
  </ul>
</main>

<footer class="site-footer abs">
  <div class="footer-left abs">Copyright © 2014 - Veskarin. - All Rights Reserved<br>Powered by: beauty center.</div>
  <div class="footer-right abs">Toll-Free: (800) 555-0199<br>Email: info@veskarin-mail.com<br>2740 N. Elm Parkway • Riverside, OK 73190</div>
</footer>

</body>
</html>
```